New Business Card Design Project for Handyman Business

I would like to purchase a customized version of a design you have previously submitted - https://www.artvelloshowcase.com/design/58172046
I love this design!
I am hoping you can design something similar to this for our Handyman Business.
Attached is our logo and some graphics we have used.
Here is a link to the Google Doc with the content that needs to be included, https://files.quorvandel.net/document/d/e/4QZTR-8kPw2LmXn5Hb7rYcVt-qaaJsK3Df9TgNpU4WeR__LmcXaBvKpHsd2Qjn7wo4tzhgrVb41K85o3ttSTq/pub
Target Market(s)
Real Estate Agents, Home Owners and Property Managers
Industry/Entity Type
Construction/ Speciality Trade
Contact Information for Business Card
https://files.quorvandel.net/document/d/7QwRtYpL_zxkn4BvHnCdFs8TmKjWaEr2LUXPo6cxhg/edit?usp=sharing
Font styles to use
Other font styles liked:
- Ubuntu
Look and feel
Each slider illustrates characteristics of the customer's brand and the style your logo design should communicate.

```html
<!DOCTYPE html>
<html lang="en">
<head>
<meta charset="utf-8">
<title>Fixwell Business Card</title>
<link href="https://fonts.googleapis.com/css2?family=Ubuntu:wght@400;500;700&display=swap" rel="stylesheet">
<style>
  :root {
    --backdrop: #ececec;
    --navy: #0f1a45;
    --navy-deep: #0b1438;
    --tone-blue: #1b3270;
    --tone-green: #1d4a4a;
    --green: #43b649;
    --blue: #1e96d6;
    --orange: #f0692d;
    --white: #f2f4f8;
    --rule: #c9cdd8;
  }
  * { box-sizing: border-box; margin: 0; padding: 0; }
  html, body { width: 1200px; height: 1200px; overflow: hidden; }
  body {
    background: var(--backdrop);
    font-family: "Ubuntu", sans-serif;
    position: relative;
  }
  .card {
    position: absolute;
    top: 215px;
    width: 440px;
    height: 770px;
    background: var(--navy);
    border-radius: 6px;
    overflow: hidden;
    box-shadow: 0 18px 40px rgba(10, 18, 54, 0.25);
  }
  .card--front { left: 120px; }
  .card--back { left: 640px; }

  .pattern-field {
    position: absolute;
    left: 0; right: 0; top: 0;
    background:
      radial-gradient(ellipse 70% 45% at 25% 20%, rgba(29, 74, 74, 0.55), transparent 70%),
      radial-gradient(ellipse 60% 40% at 80% 45%, rgba(27, 50, 112, 0.7), transparent 70%),
      linear-gradient(180deg, var(--tone-blue) 0%, rgba(15, 26, 69, 0) 100%);
  }
  .card--front .pattern-field { height: 620px; }
  .card--back .pattern-field { height: 300px; }

  .brand {
    position: absolute;
    left: 0; right: 0;
    display: flex;
    align-items: center;
    justify-content: center;
    gap: 12px;
  }
  .brand__mark {
    background: var(--blue);
  }
  .brand__name {
    color: var(--green);
    font-weight: 700;
    letter-spacing: 0.5px;
  }
  .card--front .brand { top: 410px; }
  .card--front .brand__mark { width: 26px; height: 26px; }
  .card--front .brand__name { font-size: 56px; }

  .tagline {
    position: absolute;
    top: 490px; left: 0; right: 0;
    text-align: center;
    color: var(--orange);
    font-size: 17px;
    font-weight: 500;
    letter-spacing: 3px;
  }
  .front-rule {
    position: absolute;
    top: 535px; left: 0; right: 0;
    height: 2px;
    background: var(--rule);
  }
  .hashtag {
    position: absolute;
    top: 553px; left: 0; right: 0;
    text-align: center;
    color: var(--white);
    font-size: 17px;
    font-weight: 500;
  }
  .social-row {
    position: absolute;
    top: 605px; left: 0; right: 0;
    display: flex;
    justify-content: center;
    gap: 16px;
  }
  .social-row span {
    width: 58px; height: 58px;
    border: 3px solid var(--green);
    border-radius: 50%;
    background: rgba(67, 182, 73, 0.12);
    display: flex;
    align-items: center;
    justify-content: center;
  }
  .social-row span::after {
    content: "";
    width: 16px; height: 16px;
    border-radius: 50%;
    background: var(--green);
  }

  .card--back .brand { top: 200px; }
  .card--back .brand__mark { width: 22px; height: 22px; }
  .card--back .brand__name { font-size: 42px; }
  .person {
    position: absolute;
    top: 290px; left: 0; right: 0;
    text-align: center;
  }
  .person__name {
    color: var(--white);
    font-size: 40px;
    font-weight: 500;
    letter-spacing: 1px;
  }
  .person__role {
    margin-top: 6px;
    font-size: 22px;
    font-weight: 500;
  }
  .person__role .owner { color: var(--green); }
  .person__role .trade { color: var(--blue); }
  .back-rule {
    position: absolute;
    left: 50px; right: 50px;
    height: 3px;
    background: var(--orange);
  }
  .back-rule--top { top: 400px; }
  .back-rule--bottom { top: 590px; }
  .contact {
    position: absolute;
    top: 425px; left: 0; right: 0;
    text-align: center;
    line-height: 1.45;
  }
  .contact__phone { color: var(--white); font-size: 34px; font-weight: 500; }
  .contact__email { color: var(--blue); font-size: 24px; }
  .contact__web { color: var(--green); font-size: 24px; letter-spacing: 0.5px; }
  .services {
    position: absolute;
    top: 630px; left: 0; right: 0;
    text-align: center;
  }
  .services__sector { color: var(--white); font-size: 19px; font-weight: 500; letter-spacing: 0.5px; }
  .services__list { margin-top: 10px; color: var(--blue); font-size: 17px; font-weight: 500; letter-spacing: 0.5px; }
</style>
</head>
<body>
  <section class="card card--front">
    <div class="pattern-field" role="img" aria-label="Repeating pattern of the brand symbol on navy"></div>
    <div class="brand">
      <span class="brand__mark"></span>
      <span class="brand__name">fixwell</span>
    </div>
    <p class="tagline">HOME CARE SPECIALISTS</p>
    <div class="front-rule"></div>
    <p class="hashtag">#FixwellHomeRepairServices</p>
    <div class="social-row" aria-label="Social profiles">
      <span></span><span></span><span></span><span></span>
    </div>
  </section>

  <section class="card card--back">
    <div class="pattern-field" role="img" aria-label="Repeating pattern of the brand symbol on navy"></div>
    <div class="brand">
      <span class="brand__mark"></span>
      <span class="brand__name">fixwell</span>
    </div>
    <div class="person">
      <p class="person__name">DANA WHITLOW</p>
      <p class="person__role"><span class="owner">Owner/</span> <span class="trade">Handyman</span></p>
    </div>
    <div class="back-rule back-rule--top"></div>
    <div class="contact">
      <p class="contact__phone">(555) 014-2293</p>
      <p class="contact__email">dana@fixwell-home.com</p>
      <p class="contact__web">FIXWELL-HOME.COM</p>
    </div>
    <div class="back-rule back-rule--bottom"></div>
    <div class="services">
      <p class="services__sector">COMMERCIAL &amp; RESDIENTIAL</p>
      <p class="services__list">IMPROVE - REPAIR - REMODEL - MAINTAIN</p>
    </div>
  </section>
</body>
</html>
```